Accounting Practice Business Card Design

I have a logo I am happy for you to use in the design of the Business Card.
You can edit and change colours as you please, I am not fixated on it.
I am looking for a modern and clean overall feel for the finished design.

The business is a small accounting practice who thrives on word of mouth referrals and this card will be given to all current and prospect clients.

Industry/Entity Type

Accountant

Contact Information for Business Card

Marcus Vell
Level 5, 8 Ashcombe Ridge Road
FERNMOOR RISE VIC 3187
Phone: 9481 3052
Email: mvell@qrnaccountants.com.au
Web: www.qrnaccountants.com.au

Font styles to use
Serif
Sans Serif

Colors
0555a3
3277b5
85acd3
0393ce
33a6d7
85cae6
00a990
33b8a4
9bcb3c

Requirements
Must have
• "The end to your tax problems begin with us"
• "A referral from you is our greatest compliment"
Nice to have
• Modern clean professional

```html
<!DOCTYPE html>
<html lang="en">
<head>
<meta charset="utf-8">
<title>QRN Accountants – Business Card</title>
<link rel="stylesheet" href="https://fonts.googleapis.com/css2?family=Lato:wght@400;700;900&display=swap">
<style>
  :root {
    --navy: #27477a;
    --navy-deep: #1f3c6c;
    --green: #3b7a3a;
    --white: #ffffff;
    --ink: #1c1c1c;
    --backdrop: #e6e7ea;
    --rule: #2c4a7c;
  }
  * { margin: 0; padding: 0; box-sizing: border-box; }
  html, body {
    width: 1200px; height: 1059px; overflow: hidden;
    background: var(--backdrop);
    font-family: "Lato", Arial, sans-serif;
  }
  .canvas { position: relative; width: 1200px; height: 1059px; }

  .card {
    position: absolute; left: 200px; width: 800px; height: 470px;
    box-shadow: 0 6px 18px rgba(0,0,0,.18);
    overflow: hidden;
  }

  /* Back of card */
  .card-back { top: 45px; background: var(--navy); color: var(--white); }
  .card-back .wordmark {
    position: absolute; left: 0; right: 0; top: 150px;
    text-align: center; font-weight: 900; font-size: 62px; letter-spacing: 3px;
    color: var(--white);
  }
  .card-back .taglines {
    position: absolute; left: 0; right: 0; top: 330px;
    text-align: center; font-size: 19px; letter-spacing: 1px; line-height: 1.7;
    text-transform: uppercase;
  }

  /* Front of card */
  .card-front { top: 555px; background: var(--white); color: var(--ink); }
  .card-front .wordmark {
    position: absolute; left: 50px; top: 160px;
    font-weight: 900; font-size: 32px; letter-spacing: 1.5px; line-height: 1;
    color: var(--navy); white-space: nowrap;
  }
  .holder { position: absolute; right: 55px; top: 52px; text-align: right; }
  .holder-name { font-weight: 700; font-size: 28px; color: var(--navy); }
  .holder-role { font-size: 17px; margin-top: 2px; }
  .holder-rule {
    position: absolute; right: 55px; top: 122px; width: 330px; height: 1.5px;
    background: var(--rule);
  }
  .address {
    position: absolute; right: 55px; top: 150px; text-align: right;
    font-size: 20px; line-height: 1.4; font-style: normal;
  }
  .contact-rule {
    position: absolute; left: 50px; top: 258px; width: 700px; height: 1.5px;
    background: var(--rule);
  }
  .contacts {
    position: absolute; left: 50px; top: 278px; list-style: none;
    font-size: 20px; line-height: 1.55;
  }
  .contacts li { display: flex; align-items: center; gap: 14px; }
  .contacts svg { width: 16px; height: 16px; flex: none; }
  .icon-fill { fill: var(--navy-deep); }
  .icon-line { fill: none; stroke: var(--navy-deep); stroke-width: 1.4; }
  .footer-bands { position: absolute; left: 0; bottom: 0; width: 800px; height: 40px; }
</style>
</head>
<body>
<main class="canvas">

  <section class="card card-back" aria-label="Card back">
    <div class="wordmark">QRN ACCOUNTANTS</div>
    <p class="taglines">The end to your tax problems begin with us.<br>A referral from you is our greatest compliment.</p>
  </section>

  <section class="card card-front" aria-label="Card front">
    <div class="wordmark">QRN ACCOUNTANTS</div>

    <div class="holder">
      <div class="holder-name">Marcus Vell</div>
      <div class="holder-role">Accountant</div>
    </div>
    <div class="holder-rule"></div>

    <address class="address">
      Level 5, 8 Ashcombe Ridge Road<br>Fernmoor Rise Vic 3187
    </address>

    <div class="contact-rule"></div>
    <ul class="contacts">
      <li>
        <svg viewBox="0 0 16 16" aria-hidden="true"><path class="icon-fill" d="M3.6 1.5l2.2 2.6-1.3 1.6c.9 2 2.6 3.7 4.6 4.6l1.6-1.3 2.6 2.2-1.3 2.3C6.9 14.9 1.1 9.1 1.3 2.8z"/></svg>
        <span>9481 3052</span>
      </li>
      <li>
        <svg viewBox="0 0 16 16" aria-hidden="true"><path class="icon-fill" d="M1 3h14v10H1z M2.2 4.2L8 8.6l5.8-4.4z" fill-rule="evenodd"/></svg>
        <span>mvell@qrnaccountants.com.au</span>
      </li>
      <li>
        <svg viewBox="0 0 16 16" aria-hidden="true">
          <circle class="icon-line" cx="8" cy="8" r="6.5"/>
          <ellipse class="icon-line" cx="8" cy="8" rx="2.8" ry="6.5"/>
          <line class="icon-line" x1="1.5" y1="8" x2="14.5" y2="8"/>
        </svg>
        <span>www.qrnaccountants.com.au</span>
      </li>
    </ul>

    <svg class="footer-bands" viewBox="0 0 800 40" preserveAspectRatio="none" aria-hidden="true">
      <polygon points="0,14 690,14 676,40 0,40" fill="var(--green)"/>
      <polygon points="702,0 800,0 800,40 684,40" fill="var(--navy)"/>
    </svg>
  </section>

</main>
</body>
</html>
```